Awesome Redesign of Plumbing website

A great website designer to create this page for us in Wordpress with elementor.

- You are redesigning this site: http://fjordvannservice.no/

- Brand name is : Vannkraft Rør

- You can take pictures from the website or the one i attach, or stock images or AI generated images etc.

- The main call to action is to call the phone number (+47 23 58 91 64)
So please make that a priority.
- Mobile responsiveness is very important.
- The background should be white. You can use the color code red, white and black when you create the site.

I want you to build the website with a high speed score.

Target Market(s)

Residential market in oslo, Norway

Industry/Entity Type

Plumbing

Coding

Coded - Design and coding required

Requirements
Must have
• Build with elementor (wordpress), SEO friendly, A good CTA for phone, mobile responsive. Fast loading time. A Clean design.
Should not have
• Stock images that look "fake". All pictures have an authentic feel.

```html
<!DOCTYPE html>
<html lang="no">
<head>
<meta charset="utf-8">
<title>Vannkraft Rør – Rørlegger i Oslo</title>
<link href="https://fonts.googleapis.com/css2?family=Oswald:wght@400;500;600&family=Open+Sans:ital,wght@0,400;0,600;0,700;1,400&family=Montserrat:wght@500;600;700&display=swap" rel="stylesheet">
<style>
:root{
  --red:#e10b0b;
  --red-deep:#c40000;
  --black:#0b0b0b;
  --dark:#262626;
  --ink:#2b2b2b;
  --grey:#707070;
  --mist:#edf2f7;
  --white:#ffffff;
}
*{margin:0;padding:0;box-sizing:border-box}
html,body{width:1200px;height:4505px;overflow:hidden}
body{position:relative;background:var(--white);font-family:"Open Sans",sans-serif;color:var(--ink)}
.abs{position:absolute}
.h-oswald{font-family:"Oswald",sans-serif;text-transform:uppercase}
section,header,footer{position:absolute;left:0;width:1200px;overflow:visible}

/* header */
.site-header{top:0;height:115px;background:var(--white);z-index:5}
.brand{left:96px;top:30px;font-family:"Oswald",sans-serif;font-weight:600;font-size:36px;color:var(--red);letter-spacing:.5px}
.topbar{left:763px;top:0;width:395px;height:35px}
.topbar .phone{position:absolute;left:210px;top:5px;color:#fff;font-family:"Oswald",sans-serif;font-size:18px;font-weight:500;display:flex;gap:8px;align-items:center}
.nav{left:0;top:68px;font-family:"Oswald",sans-serif;font-size:15px;color:#1a1a1a}
.nav span{position:absolute;white-space:nowrap;text-transform:uppercase}
.nav .active{color:var(--red)}
.nav-underline{left:471px;top:108px;width:46px;height:3px;background:var(--red)}

/* hero */
.hero{top:115px;height:620px;background:linear-gradient(180deg,#f11111 0%,#e00808 60%,#d10000 100%)}
.hero-city{left:0;bottom:0;width:1200px;height:300px;background:linear-gradient(180deg,rgba(180,0,0,0) 0%,rgba(170,0,0,.45) 100%)}
.hero-title{left:108px;top:168px;font-size:38px;color:#fff;font-weight:500;z-index:2;white-space:nowrap}
.hero-sub{left:108px;top:222px;font-size:40px;color:#fff;font-weight:500;white-space:nowrap}
.hero-text{left:108px;top:289px;font-size:14px;color:#fff}
.btn{position:absolute;font-family:"Oswald",sans-serif;text-transform:uppercase;font-weight:600;letter-spacing:2px;display:flex;align-items:center;justify-content:center;font-size:14px}
.btn-black{background:var(--black);color:#fff}
.btn-red{background:var(--red);color:#fff}
.btn-frame::after{content:"";position:absolute;left:-5px;top:-5px;right:5px;bottom:5px;border:2px solid var(--red);border-bottom:none;border-right:none;z-index:-1}
.van{border-radius:40px 60px 30px 30px;background:linear-gradient(160deg,#3a3a3a,#0d0d0d 70%);box-shadow:0 12px 20px rgba(0,0,0,.25)}

.quote-form{left:752px;top:95px;width:290px;height:411px;background:var(--black);color:#fff;text-align:center}
.quote-form h3{font-family:"Oswald",sans-serif;font-weight:500;font-size:24px;margin-top:22px;letter-spacing:.5px}
.quote-form p{font-size:11px;margin-top:2px}
.field{position:absolute;left:31px;width:233px;background:#fff;color:#666;font-size:10.5px;text-align:left;padding:9px 10px 0 32px}
.field svg{position:absolute;left:10px;top:9px}
.form-btn{left:31px;top:343px;width:233px;height:36px}

/* about */
.about-photo{left:117px;top:110px;width:500px;height:316px;background:linear-gradient(135deg,#9a9a9a,#3b3b3b 60%,#1b1b1b)}
.play{left:117px;top:381px;width:63px;height:45px;background:var(--red);display:flex;align-items:center;justify-content:center}
.sec-title{font-family:"Oswald",sans-serif;font-weight:500;color:var(--red);text-transform:uppercase}
.about-title{left:675px;top:100px;font-size:44px;white-space:nowrap}
.about-lead{left:675px;top:170px;width:430px;font-size:14px;font-weight:700;line-height:22px;color:#333}
.about-body{left:675px;top:258px;width:430px;font-size:14px;line-height:21px;color:var(--grey)}

/* services */
.services{top:1247px;height:813px;background:var(--mist)}
.kicker{left:0;width:1200px;text-align:center;font-family:"Oswald",sans-serif;font-size:17px;letter-spacing:3px;color:#222}
.center-title{left:0;width:1200px;text-align:center;font-size:44px}
.ring{left:127px;top:213px;width:436px;height:436px;border-radius:50%;border:3px solid #dfe5ec;background:var(--mist)}
.ring-photo{left:152px;top:236px;width:386px;height:386px;border-radius:50%;background:radial-gradient(circle at 50% 40%,#ff2a2a,#d50000 70%)}
.dot{width:14px;height:14px;border-radius:50%;background:var(--red);border:3px solid var(--mist)}
.svc-icon{width:76px;height:76px;border-radius:50%;background:#fff;box-shadow:0 4px 12px rgba(0,0,0,.08);display:flex;align-items:center;justify-content:center}
.svc h4{font-family:"Oswald",sans-serif;font-weight:400;font-size:17px;letter-spacing:3px;color:#222}
.svc p{font-size:11px;line-height:17px;color:var(--grey);width:440px;margin-top:5px}

/* miljø */
.env{top:2060px;height:523px;background:#fff}
.env-photo{left:0;top:0;width:1200px;height:523px;background:linear-gradient(120deg,#dcdcdc,#8d8d8d 55%,#b81818 80%,#5a5a5a);clip-path:polygon(805px 0,1200px 0,1200px 523px,495px 523px)}
.env-title{left:114px;top:88px;font-size:34px}
.env-text{left:114px;top:142px;width:446px;font-size:12.5px;line-height:23px;color:var(--grey);text-align:justify}

/* testimonials */
.reviews{top:2583px;height:522px;background:linear-gradient(180deg,#1f1f1f,#2f2f2f)}
.reviews-red{left:0;top:0;width:1200px;height:522px;background:linear-gradient(180deg,#e80b0b,#c40000);clip-path:polygon(0 0,411px 0,0 443px)}
.reviews-city{left:0;bottom:0;width:1200px;height:180px;background:linear-gradient(180deg,rgba(0,0,0,0),rgba(0,0,0,.35))}
.card{width:301px;height:229px;background:#fff;border-bottom:4px solid var(--red);padding:32px 32px 0}
.card p{font-size:11px;font-style:italic;line-height:21px;color:#555}
.card .who{position:absolute;left:32px;top:158px;display:flex;align-items:center;gap:14px}
.avatar{width:30px;height:30px;border-radius:50%;background:linear-gradient(135deg,#c9c9c9,#7b7b7b)}
.who b{display:block;font-family:"Montserrat",sans-serif;font-size:11px;color:#222}
.stars{color:#f4b400;font-size:14px;letter-spacing:2px}

/* tidlig */
.trust-photo{left:131px;top:78px;width:385px;height:458px;background:linear-gradient(180deg,#e02020 0%,#c52a2a 25%,#8a2f2f 60%,#3f3a3a 100%);border-radius:90px 90px 0 0}
.trust-title{left:614px;top:172px;font-size:34px;white-space:nowrap}
.trust-text{left:614px;top:225px;width:560px;font-size:14px;line-height:23px;color:#444}

/* contact */
.contact{top:3641px;height:410px;background:var(--mist)}
.c-icon{width:72px;height:72px;border-radius:50%;background:var(--red);display:flex;align-items:center;justify-content:center;box-shadow:0 6px 12px rgba(200,0,0,.25)}
.c-text{width:300px;text-align:center;font-size:15px;line-height:25px;color:#333}

/* footer */
.site-footer{top:4051px;height:454px;background:var(--red-deep);color:#fff;font-family:"Montserrat",sans-serif}
.f-head{font-family:"Oswald",sans-serif;font-weight:500;font-size:19px;text-transform:uppercase;white-space:nowrap}
.f-list{font-size:12px;line-height:22px;font-weight:500;white-space:nowrap}
.map{left:498px;top:117px;width:301px;height:190px;background:linear-gradient(135deg,#f1f1f1,#d9d9d9);border:1px solid #fff}
.f-social{width:18px;height:18px;border-radius:50%;background:#fff}
.f-contact{white-space:nowrap}
.f-contact b{display:block;font-size:12px;font-weight:700}
.f-contact span{font-size:12px;line-height:22px;font-weight:500}
.f-rule{left:0;top:386px;width:1200px;height:1px;background:rgba(255,255,255,.25)}
.f-copy{top:406px;font-size:11px;font-weight:500;white-space:nowrap}
</style>
</head>
<body>

<header class="site-header">
  <div class="brand abs">VANNKRAFT RØR</div>
  <svg class="topbar abs" width="395" height="35" viewBox="0 0 395 35" aria-hidden="true">
    <polygon points="8,0 192,0 186,35 0,35" fill="#0b0b0b"/>
    <polygon points="192,0 395,0 386,35 186,35" fill="#e10b0b"/>
    <circle cx="40" cy="17" r="6" fill="#fff"/>
    <circle cx="77" cy="17" r="6" fill="#fff"/>
    <circle cx="118" cy="17" r="6" fill="#fff"/>
    <rect x="150" y="11" width="16" height="12" fill="#fff"/>
    <polyline points="150,11 158,18 166,11" fill="none" stroke="#0b0b0b" stroke-width="1.5"/>
  </svg>
  <div class="topbar abs">
    <div class="phone">
      <svg width="18" height="18" viewBox="0 0 24 24"><path d="M6.6 10.8a15 15 0 0 0 6.6 6.6l2.2-2.2a1 1 0 0 1 1-.25 11.4 11.4 0 0 0 3.6.57 1 1 0 0 1 1 1V20a1 1 0 0 1-1 1A17 17 0 0 1 3 4a1 1 0 0 1 1-1h3.5a1 1 0 0 1 1 1c0 1.25.2 2.45.57 3.57a1 1 0 0 1-.25 1z" fill="none" stroke="#fff" stroke-width="1.8"/></svg>
      +47 23 58 91 64
    </div>
  </div>
  <nav class="nav abs">
    <span class="active" style="left:476px">Hjem</span>
    <span style="left:563px">Om oss</span>
    <span style="left:666px">Tjenester</span>
    <span style="left:787px">Miljø og kvalitet</span>
    <span style="left:962px">Attester</span>
    <span style="left:1077px">Kontakt</span>
  </nav>
  <div class="nav-underline abs"></div>
</header>

<section class="hero">
  <div class="hero-city abs" role="img" aria-label="Faint red city skyline silhouette"></div>
  <svg class="abs" style="left:79px;top:179px" width="622" height="44" viewBox="0 0 622 44" aria-hidden="true">
    <polygon points="14,2 600,2 600,0 622,22 600,44 600,40 0,40" fill="#0b0b0b"/>
  </svg>
  <div class="hero-title abs h-oswald">Velkommen til Vannkraft Rør</div>
  <div class="hero-sub abs h-oswald">Rorservice Vannkraft Rør</div>
  <div class="hero-text abs">Vi hjelper deg med alt arbeid relatert til Rørlegging,</div>
  <div class="btn btn-black" style="left:110px;top:322px;width:165px;height:40px">Kontakt</div>
  <div class="van abs" style="left:184px;top:424px;width:441px;height:251px;z-index:3" role="img" aria-label="Black company service van with red pipe graphics"></div>

  <form class="quote-form abs">
    <h3>SPØRRESKJEMA</h3>
    <p>Get free quote now from our expert</p>
    <div class="field" style="top:93px;height:35px"><svg width="14" height="14" viewBox="0 0 24 24"><circle cx="12" cy="8" r="4" fill="none" stroke="#777" stroke-width="2"/><path d="M4 21c1-4 4-6 8-6s7 2 8 6" fill="none" stroke="#777" stroke-width="2"/></svg>Your Name</div>
    <div class="field" style="top:136px;height:34px"><svg width="14" height="14" viewBox="0 0 24 24"><rect x="3" y="6" width="18" height="12" fill="none" stroke="#777" stroke-width="2"/><polyline points="3,6 12,13 21,6" fill="none" stroke="#777" stroke-width="2"/></svg>Email Address</div>
    <div class="field" style="top:180px;height:33px"><svg width="14" height="14" viewBox="0 0 24 24"><path d="M6.6 10.8a15 15 0 0 0 6.6 6.6l2.2-2.2 4.6.6V20A17 17 0 0 1 3 4h4.3l.6 4.6z" fill="none" stroke="#777" stroke-width="2"/></svg>Phone Number</div>
    <div class="field" style="top:222px;height:33px"><svg width="14" height="14" viewBox="0 0 24 24"><circle cx="12" cy="12" r="9" fill="none" stroke="#777" stroke-width="2"/><polyline points="8,12 11,15 16,9" fill="none" stroke="#777" stroke-width="2"/></svg>Contact Prefer time</div>
    <div class="field" style="top:264px;height:66px"><svg width="14" height="14" viewBox="0 0 24 24"><circle cx="12" cy="12" r="9" fill="none" stroke="#777" stroke-width="2"/><line x1="8" y1="12" x2="16" y2="12" stroke="#777" stroke-width="2"/></svg>Your Message</div>
    <div class="btn btn-red form-btn">Sende melding</div>
  </form>
</section>

<section class="about" style="top:735px;height:512px">
  <div class="about-photo abs" role="img" aria-label="Two plumbers standing in front of the company van"></div>
  <div class="play abs"><svg width="20" height="22" viewBox="0 0 20 22"><polygon points="2,1 19,11 2,21" fill="#fff"/></svg></div>
  <h2 class="about-title abs sec-title">Om Vannkraft Rør</h2>
  <p class="about-lead abs">I flere år har huseiere og bedrifter i hele Oslo regnet med at Vannkraft Rør for å tilby profesjonelle rørleggingstjenester. Vi er uslåelige når det gjelder erfaring, tilgjengelighet og overkommelig pris!</p>
  <p class="about-body abs">Mange år i bransjen har gitt oss erfaringen du trenger for å få et vellykket resultat. Vi kommer gjerne på en befaring for å komme opp med et forslag på hva tror vi gi det beste resultatet. Vår erfaring er at det er detaljene som skiller "mesteren" fra resten, og vi vet hvilke detaljer som teller.</p>
  <div class="btn btn-black btn-frame" style="left:677px;top:381px;width:154px;height:38px;z-index:1">Lære mer</div>
</section>

<section class="services">
  <div class="kicker abs" style="top:46px">HVA VI GJØR</div>
  <h2 class="center-title abs sec-title" style="top:76px">Våre tjenester</h2>
  <div class="ring abs"></div>
  <div class="ring-photo abs" role="img" aria-label="Plumber working under a sink, red-toned"></div>
  <div class="van abs" style="left:206px;top:502px;width:287px;height:152px" role="img" aria-label="Black company van"></div>
  <div class="dot abs" style="left:484px;top:261px"></div>
  <div class="dot abs" style="left:546px;top:350px"></div>
  <div class="dot abs" style="left:556px;top:446px"></div>
  <div class="dot abs" style="left:525px;top:542px"></div>

  <div class="svc-icon abs" style="left:520px;top:189px"><svg width="36" height="36" viewBox="0 0 36 36" fill="none" stroke="#e10b0b" stroke-width="2"><path d="M6 30V18h10v-6h14"/><path d="M12 30V22h10v-6h8"/><circle cx="30" cy="14" r="3"/></svg></div>
  <div class="svc abs" style="left:617px;top:200px"><h4>BRANNVERN</h4><p>Lorem ipsum dolor sit amet, consectetur adipiscing elit, sed do eiusmod tempor incididunt ut labore et dolore magna aliqua. Ut enim ad minim veniam</p></div>

  <div class="svc-icon abs" style="left:593px;top:310px"><svg width="36" height="36" viewBox="0 0 36 36" fill="none" stroke="#e10b0b" stroke-width="2"><path d="M8 10h14v6H8z"/><path d="M22 13h6v14"/><path d="M12 16v10h6"/><circle cx="28" cy="29" r="2"/></svg></div>
  <div class="svc abs" style="left:689px;top:318px"><h4>SERVICE OG VEDLIKEHOLD</h4><p style="width:380px">Lorem ipsum dolor sit amet, consectetur adipiscing elit, sed do eiusmod tempor incididunt ut labore et dolore magna</p></div>

  <div class="svc-icon abs" style="left:606px;top:429px"><svg width="36" height="36" viewBox="0 0 36 36" fill="none" stroke="#e10b0b" stroke-width="2"><circle cx="18" cy="10" r="5"/><path d="M8 32c0-8 4-13 10-13s10 5 10 13"/><path d="M22 24l6-6"/></svg></div>
  <div class="svc abs" style="left:694px;top:440px"><h4>RØRLEGGERVAKT</h4><p style="width:390px">Lorem ipsum dolor sit amet, consectetur adipiscing elit, sed do eiusmod tempor incididunt ut labore et dolore magna aliqua.</p></div>

  <div class="svc-icon abs" style="left:562px;top:546px"><svg width="36" height="36" viewBox="0 0 36 36" fill="none" stroke="#e10b0b" stroke-width="2"><rect x="6" y="12" width="24" height="16" rx="2"/><line x1="11" y1="12" x2="11" y2="28"/><line x1="16" y1="12" x2="16" y2="28"/><line x1="21" y1="12" x2="21" y2="28"/><line x1="26" y1="12" x2="26" y2="28"/><path d="M10 12V8h16"/></svg></div>
  <div class="svc abs" style="left:656px;top:560px"><h4>RADIATOR</h4><p style="width:420px">Lorem ipsum dolor sit amet, consectetur adipiscing elit, sed do eiusmod tempor incididunt ut labore et dolore magna aliqua. Ut enim</p></div>

  <div class="btn btn-black btn-frame" style="left:526px;top:689px;width:149px;height:37px;z-index:1">Lære mer</div>
</section>

<section class="env">
  <div class="env-photo abs" role="img" aria-label="Grey-bearded plumber in red shirt sealing a pipe thread in a workshop"></div>
  <h2 class="env-title abs sec-title">Miljø og kvalitet</h2>
  <p class="env-text abs">Enten du skal pusse opp, renovere eller du opplever lekkasjer eller skader på eksisterende rørsystemer, så er trenger du rørlegger i Oslo som du kan stole på og som stiller til avtalt tid. Arbeid med rørlegging blir raskt kostbart, og en billig rørlegger vil gjøre at du kan spare på utgiftene og dermed få utført prosjektet slik du ønsker.<br>Prosjekter i nybygg er ofte en del annerledes enn når man pusser opp eller renoverer. I nybygg tilpasses byggeprosessen slik at det blir så enkelt som mulig å sikre at badet er tett, mens renovering og oppussing må tilpasses rundt eksisterende konstruksjon. I mange tilfeller kan</p>
  <div class="btn btn-red btn-frame" style="left:116px;top:381px;width:152px;height:38px;z-index:1">Lære mer</div>
</section>

<section class="reviews">
  <div class="reviews-red abs"></div>
  <div class="reviews-city abs" role="img" aria-label="Faint dark city skyline silhouette"></div>
  <div class="abs h-oswald" style="left:117px;top:135px;color:#fff;font-size:16px;letter-spacing:1px">Attester</div>
  <h2 class="abs h-oswald" style="left:117px;top:158px;color:#fff;font-size:34px;font-weight:500;line-height:46px">Hva vår<br>sier kunden</h2>
  <div class="btn abs" style="left:115px;top:270px;width:179px;height:40px;background:#fff;color:#111;font-size:12px;border-left:3px solid #111">Se alle anmeldelser</div>
  <div class="van abs" style="left:105px;top:361px;width:371px;height:204px;z-index:2" role="img" aria-label="Black company van, mirrored"></div>

  <div class="card abs" style="left:453px;top:126px">
    <p>"Lorem ipsum dolor sit amet, consectetur adipiscing elit, sed do eiusmod tempor incididunt ut labore et dolore magna aliqua. Ut enim ad minim veniam, quis nostrud exercitation"</p>
    <div class="who"><div class="avatar" role="img" aria-label="Customer portrait"></div><div><b>EIRIK LUNDE</b><span class="stars">★★★★★</span></div></div>
  </div>
  <div class="card abs" style="left:798px;top:126px">
    <p>"Lorem ipsum dolor sit amet, consectetur adipiscing elit, sed do eiusmod tempor incididunt ut labore et dolore magna aliqua. Ut enim ad minim veniam, quis nostrud exercitation"</p>
    <div class="who"><div class="avatar" role="img" aria-label="Customer portrait"></div><div><b>EIRIK LUNDE</b><span class="stars">★★★★★</span></div></div>
  </div>
</section>

<section class="trust" style="top:3105px;height:536px">
  <div class="trust-photo abs" role="img" aria-label="Plumber in red hard hat and checked shirt holding a large pipe wrench"></div>
  <h2 class="trust-title abs sec-title">Tidlig. Ærlig. Profesjonell.</h2>
  <p class="trust-text abs">Når man skal pusse opp bad eller våtrom, kan rørleggerfirmaet ta ansvar for hele prosjektet og koordinere arbeid som<br>&nbsp;må utføres av andre typer håndverkere.<br>Rørleggere tetter og behandler overflater slik at man ikke risikerer lekkasjer og kan benytte bader</p>
  <div class="btn btn-black btn-frame" style="left:624px;top:367px;width:284px;height:47px;z-index:1">Avtale en time</div>
</section>

<section class="contact">
  <div class="kicker abs" style="top:70px">HVA VI GJØR</div>
  <h2 class="center-title abs sec-title" style="top:100px">Våre tjenester</h2>
  <div class="c-icon abs" style="left:321px;top:169px"><svg width="34" height="34" viewBox="0 0 24 24" fill="none" stroke="#fff" stroke-width="1.5"><path d="M12 22s7-7 7-12a7 7 0 0 0-14 0c0 5 7 12 7 12z"/><circle cx="12" cy="10" r="2.5"/></svg></div>
  <div class="c-icon abs" style="left:585px;top:169px"><svg width="34" height="34" viewBox="0 0 24 24" fill="none" stroke="#fff" stroke-width="1.5"><path d="M6.6 10.8a15 15 0 0 0 6.6 6.6l2.2-2.2a1 1 0 0 1 1-.25 11.4 11.4 0 0 0 3.6.57 1 1 0 0 1 1 1V20a1 1 0 0 1-1 1A17 17 0 0 1 3 4a1 1 0 0 1 1-1h3.5a1 1 0 0 1 1 1c0 1.25.2 2.45.57 3.57a1 1 0 0 1-.25 1z"/></svg></div>
  <div class="c-icon abs" style="left:847px;top:169px"><svg width="36" height="36" viewBox="0 0 24 24" fill="none" stroke="#fff" stroke-width="1.5"><rect x="3" y="6" width="18" height="12"/><polyline points="3,6 12,13 21,6"/><line x1="3" y1="18" x2="10" y2="12"/><line x1="21" y1="18" x2="14" y2="12"/></svg></div>
  <div class="c-text abs" style="left:207px;top:250px">Plassering:<br>Kirkeveien 14B Oslo 0368<br>23 58 91 64</div>
  <div class="c-text abs" style="left:471px;top:250px">Telefon:<br>+47 23 58 91 64</div>
  <div class="c-text abs" style="left:733px;top:254px">E-post:<br>info@fjordvannservice.no</div>
</section>

<footer class="site-footer">
  <div class="f-head abs" style="left:143px;top:66px">Navigasjon</div>
  <div class="f-list abs" style="left:143px;top:112px">HJEM<br>OM OSS<br>TJENESTER<br>MILJØ OG KVALITET<br>attester<br>KONTAKT</div>
  <div class="f-social abs" style="left:138px;top:304px"></div>
  <div class="f-social abs" style="left:178px;top:304px"></div>
  <div class="f-social abs" style="left:218px;top:304px"></div>
  <svg class="abs" style="left:258px;top:306px" width="18" height="14" viewBox="0 0 18 14"><rect width="18" height="14" fill="#fff"/><polyline points="0,0 9,7 18,0" fill="none" stroke="#c40000" stroke-width="1.5"/></svg>

  <div class="f-head abs" style="left:325px;top:66px">Tjenester</div>
  <div class="f-list abs" style="left:325px;top:114px">Brannvern<br>Industri<br>Service og vedlikehold<br>Rørleggervakt<br>Pusse opp bad Oslo<br>Varmepumpe<br>Radiator<br>Rens av rør oslo</div>

  <div class="f-head abs" style="left:495px;top:66px">Vår beliggenhet</div>
  <div class="map abs" role="img" aria-label="Street map of central Oslo with a red location pin"></div>

  <div class="f-head abs" style="left:871px;top:66px">Kontakt oss</div>
  <svg class="abs" style="left:870px;top:116px" width="24" height="28" viewBox="0 0 24 28"><path d="M12 27s10-10 10-16a10 10 0 0 0-20 0c0 6 10 16 10 16z" fill="#fff"/><circle cx="12" cy="11" r="3.5" fill="#c40000"/></svg>
  <div class="f-contact abs" style="left:912px;top:114px"><b>ADRESSE</b><span>Kirkeveien 14B Oslo 0368<br>23 58 91 64</span></div>
  <svg class="abs" style="left:870px;top:196px" width="26" height="26" viewBox="0 0 24 24" fill="none" stroke="#fff" stroke-width="1.8"><path d="M6.6 10.8a15 15 0 0 0 6.6 6.6l2.2-2.2a1 1 0 0 1 1-.25 11.4 11.4 0 0 0 3.6.57 1 1 0 0 1 1 1V20a1 1 0 0 1-1 1A17 17 0 0 1 3 4a1 1 0 0 1 1-1h3.5a1 1 0 0 1 1 1c0 1.25.2 2.45.57 3.57a1 1 0 0 1-.25 1z"/></svg>
  <div class="f-contact abs" style="left:912px;top:196px"><b>TELEFONNUMMER</b><span>+47 23 58 91 64</span></div>
  <svg class="abs" style="left:870px;top:252px" width="28" height="28" viewBox="0 0 24 24" fill="none" stroke="#fff" stroke-width="1.8"><circle cx="12" cy="12" r="9"/><polyline points="7,12 11,16 20,5"/></svg>
  <div class="f-contact abs" style="left:912px;top:252px"><b>ARBEIDSTID</b><span>Mon- Fri: 7:00 Am to 9:00 Pm<br>Sat-Sun: 8:00 Am to 5:00 Pm</span></div>

  <div class="f-rule abs"></div>
  <div class="f-copy abs" style="left:136px">© 2023 Vannkraft Rør Alle rettigheter reservert.</div>
  <div class="f-copy abs" style="left:918px">Policy Privacy &nbsp;|&nbsp; Terms of Use</div>
</footer>

</body>
</html>
```